Brochure Cover and Back pages

We are a US-based cosmetics company that sells state-of-the-art skin care products, including advanced anti-aging serums, natural mineral sunscreens, organic antioxidant moisturizers, and organic face cleansers. We need a product brochure. We already have chosen a design for the layout of the product info pages. But we still need a cover page and a back page. We are looking for simple but elegant design for the cover page. The back page is less important and we already know what we want on the back page. It will be the company's mission statement and at the bottom, the company URL, phone number, etc.

The brochure has two folds. So there will be three panels on both sides. The size of each panel is 16.5 (l) x 9.5 (w) cm.

At the end of the project, we expect the designer to integrate all the pages so that the finished copy is read to be sent off to a printing service for printing.

All the product info pages are attached. Also attached are the text (info) to go on the back page, company logo with and without the tagline, the icon in the logo.

YOu are welcome to visit our website www.morvask.com to learn about our products.

Industry/Entity Type

Cosmetics

```html
<!DOCTYPE html>
<html lang="en">
<head>
<meta charset="utf-8">
<title>Morvask Brochure – Cover and Back</title>
<link rel="stylesheet" href="https://fonts.googleapis.com/css2?family=Roboto+Condensed:wght@700&family=Open+Sans:wght@400;600;700&family=Bodoni+Moda:wght@500&family=Comfortaa:wght@400&display=swap">
<style>
  :root {
    --ink: #1a1a1a;
    --blue: #1f4fa0;
    --pink: #e680b4;
    --pink-soft: #f6d3dc;
    --pink-pale: #fcecef;
    --grey-band: #e7e7ea;
    --white: #ffffff;
  }
  * { margin: 0; padding: 0; box-sizing: border-box; }
  html, body { width: 1200px; height: 695px; overflow: hidden; background: var(--white); }
  .brochure { position: relative; width: 1200px; height: 695px; display: flex; font-family: "Open Sans", Arial, sans-serif; color: var(--ink); }
  .panel { position: relative; width: 400px; height: 695px; overflow: hidden; }

  /* Left panel: cleanser listing */
  .panel--products { background: var(--white); }
  .range-title { position: absolute; left: 17px; top: 18px; font-family: "Roboto Condensed", "Arial Narrow", sans-serif; font-size: 22px; line-height: 28px; color: var(--blue); }
  .range-subtitle { position: absolute; left: 17px; top: 49px; font-size: 13px; line-height: 18px; color: var(--blue); }
  .product { position: absolute; left: 0; width: 400px; }
  .product--refresh { top: 96px; height: 172px; }
  .product--hydrate { top: 268px; height: 188px; background: var(--grey-band); }
  .product--milk { top: 456px; height: 190px; }
  .product__name { position: absolute; left: 17px; font-size: 14.5px; line-height: 20px; font-weight: 700; white-space: nowrap; }
  .product__copy { position: absolute; left: 17px; font-size: 13.4px; line-height: 18.2px; white-space: nowrap; }
  .product--refresh .product__name { top: 16px; }
  .product--refresh .product__copy { top: 44px; }
  .product--hydrate .product__name { top: 32px; }
  .product--hydrate .product__copy { top: 63px; }
  .product--milk .product__name { top: 43px; }
  .product--milk .product__copy { top: 72px; }
  .product__shot { position: absolute; border-radius: 6px 6px 14px 14px; background: linear-gradient(180deg, #f4f6f9, #dfe5ec); }
  .product--refresh .product__shot { left: 303px; top: 4px; width: 58px; height: 150px; }
  .product--hydrate .product__shot { left: 300px; top: 12px; width: 62px; height: 160px; }
  .product--milk .product__shot { left: 305px; top: 28px; width: 58px; height: 148px; }
  .panel-footer { position: absolute; left: 0; width: 400px; top: 660px; text-align: center; font-size: 15px; line-height: 20px; }

  /* Middle panel: back page */
  .panel--back { background: linear-gradient(180deg, #fdf4f5 0%, #fae3e8 35%, #f6d2da 100%); }
  .back-brand { position: absolute; left: 0; width: 400px; top: 150px; text-align: center; font-family: "Bodoni Moda", Georgia, serif; font-weight: 500; font-size: 62px; line-height: 1; color: var(--ink); letter-spacing: 1px; }
  .swoosh { position: absolute; left: 0; }
  .mission { position: absolute; left: 0; width: 400px; top: 374px; text-align: center; font-family: "Comfortaa", Verdana, sans-serif; font-size: 20.5px; line-height: 33px; color: var(--pink); letter-spacing: 0.5px; }
  .contact { position: absolute; left: 0; width: 400px; text-align: center; font-weight: 700; font-size: 16.5px; line-height: 21px; color: var(--pink); }
  .contact--web { top: 496px; }
  .contact--service { top: 539px; }
  .contact--address { top: 603px; }

  /* Right panel: cover */
  .panel--cover { position: absolute; left: 800px; top: 0; background: var(--white); }
  .cover-brand { position: absolute; left: 824px; top: 46px; font-family: "Bodoni Moda", Georgia, serif; font-weight: 500; font-size: 42px; line-height: 1; color: var(--ink); white-space: nowrap; }
  .cover-tagline { position: absolute; left: 851px; top: 89px; font-family: "Comfortaa", Verdana, sans-serif; font-size: 13.5px; line-height: 17px; color: var(--ink); white-space: nowrap; }
  .cover-portrait { position: absolute; left: 898px; top: 118px; width: 302px; height: 330px; background: radial-gradient(ellipse at 62% 45%, #f3d9cb 0%, #ecd2c4 45%, #f7ece6 75%, #ffffff 100%); }
  .cover-range { position: absolute; left: 972px; top: 472px; width: 176px; height: 172px; border-radius: 10px; background: linear-gradient(180deg, #f2f6fa, #e3e8ee 70%, #f3e4e4); }
  .cover-web { position: absolute; left: 800px; width: 400px; top: 662px; text-align: center; font-size: 16.5px; line-height: 22px; color: var(--pink); }
  .cover-base { position: absolute; left: 800px; top: 640px; width: 400px; height: 55px; background: linear-gradient(180deg, #ffffff, #fbe6ea); }
</style>
</head>
<body>
<main class="brochure">

  <section class="panel panel--products">
    <h2 class="range-title">Organic Face Cleansers</h2>
    <p class="range-subtitle">Gentle for All Skin Types</p>

    <article class="product product--refresh">
      <h3 class="product__name">Refreshing Natural Cleanser</h3>
      <p class="product__copy">This refreshing aloe-based gel cleanser is<br>formulated with organic ingredients. It<br>cleans thoroughly without drying out<br>the skin. Balances skin hydration and<br>sebum.&nbsp; 4 fl. oz.</p>
      <div class="product__shot" role="img" aria-label="Product photo: white tube of Refreshing Natural Cleanser"></div>
    </article>

    <article class="product product--hydrate">
      <h3 class="product__name">Hydrating Organic Cleanser</h3>
      <p class="product__copy">This light gel cleanser is formulated with<br>coconut milk and honey for a<br>moisturizing wash. Gently washes away<br>dirt and oil, leaving skin hydrated and<br>softened.&nbsp; 4 fl. oz.</p>
      <div class="product__shot" role="img" aria-label="Product photo: white tube of Hydrating Organic Cleanser"></div>
    </article>

    <article class="product product--milk">
      <h3 class="product__name">Nourishing Cleansing Milk</h3>
      <p class="product__copy">This comforting organic lotion cleanser is<br>enriched with botanical extracts to leave<br>skin feeling smooth and soft. Can be<br>used to remove eye makeup.&nbsp; 4 fl. oz.</p>
      <div class="product__shot" role="img" aria-label="Product photo: white tube of Nourishing Cleansing Milk"></div>
    </article>

    <p class="panel-footer">www.morvask.com&nbsp; 1-855-5-Morvask</p>
  </section>

  <section class="panel panel--back">
    <h1 class="back-brand">Morvask</h1>
    <svg class="swoosh" style="top:240px" width="400" height="100" viewBox="0 0 400 100" aria-hidden="true">
      <path d="M0 34 C120 20 260 14 400 22" fill="none" stroke="#ffffff" stroke-width="2"/>
      <path d="M0 40 C130 26 270 22 400 30" fill="none" stroke="#f2b9c6" stroke-width="1.5"/>
      <path d="M0 88 C110 60 250 40 400 34" fill="none" stroke="#ffffff" stroke-width="2.5"/>
      <path d="M0 94 C120 66 260 46 400 40" fill="none" stroke="#f0b0bf" stroke-width="1.5"/>
    </svg>
    <p class="mission">Creating Beauty Solutions<br>through Science</p>
    <p class="contact contact--web">www.morvask.com</p>
    <p class="contact contact--service">Customer Service<br>1-855-5-Morvask (855-555-0142)</p>
    <p class="contact contact--address">1620 Larkspur Ave.&nbsp; Suite 400<br>Fairbrook, CA 94610</p>
  </section>

  <section class="panel panel--cover"></section>
  <div class="cover-portrait" role="img" aria-label="Photo: smiling woman touching her cheek, soft skin tones"></div>
  <p class="cover-brand">Morvask</p>
  <p class="cover-tagline">Bringing You Smart Skin Care</p>
  <svg class="swoosh" style="left:800px;top:428px" width="400" height="60" viewBox="0 0 400 60" aria-hidden="true">
    <path d="M0 36 C120 20 260 12 400 14" fill="none" stroke="#f4c3cf" stroke-width="2"/>
    <path d="M0 44 C130 28 270 22 400 24" fill="none" stroke="#f8d9e0" stroke-width="1.5"/>
  </svg>
  <div class="cover-base"></div>
  <div class="cover-range" role="img" aria-label="Product photo: group of skin care tubes, bottles and a cream jar"></div>
  <p class="cover-web">www.morvask.com</p>

</main>
</body>
</html>
```